construction company offering modern and striking homes and apartments

I need a card design for my new construction company called Talmont Constructions (vic) Pty Ltd.
We build everything from multi home development sites to modern and edgy apartment complexes.
I am open to any colors used as long as it stands out and doesn't look cheap. I want the final design to show my prospective clients I am a professional construction company

Industry/Entity Type

Construction

```html
<!DOCTYPE html>
<html lang="en">
<head>
<meta charset="utf-8">
<title>Talmont Constructions – Business Card</title>
<link rel="stylesheet" href="https://fonts.googleapis.com/css2?family=Josefin+Sans:wght@300;400&family=Arimo:wght@400&display=swap">
<style>
  :root {
    --stage: #5f5f5f;
    --card: #ffffff;
    --ink: #1c1a1a;
    --mark: #231f20;
    --brand-red: #82181e;
    --band-grey: #4a4a45;
    --rule: #a8a8a8;
  }
  * { margin: 0; padding: 0; box-sizing: border-box; }
  html, body {
    width: 1200px;
    height: 686px;
    overflow: hidden;
    background: var(--stage);
  }
  .stage {
    position: relative;
    width: 1200px;
    height: 686px;
  }
  .card {
    position: absolute;
    width: 486px;
    height: 277px;
    background: var(--card);
    overflow: hidden;
  }
  .card--front { left: 61px; top: 69px; }
  .card--back  { left: 595px; top: 334px; }

  .brand {
    position: absolute;
    display: flex;
    align-items: center;
  }
  .brand__dot {
    border-radius: 50%;
    background: var(--mark);
    flex: none;
  }
  .brand__name {
    font-family: "Josefin Sans", sans-serif;
    font-weight: 400;
    color: var(--ink);
    text-transform: uppercase;
    letter-spacing: 0.02em;
  }

  .card--front .brand { left: 17px; top: 86px; }
  .card--front .brand__dot { width: 64px; height: 64px; margin-right: 13px; }
  .card--front .brand__name { font-size: 16px; line-height: 16px; padding-top: 4px; }

  .card--back .brand { left: 61px; top: 76px; }
  .card--back .brand__dot { width: 108px; height: 108px; margin-right: 19px; }
  .card--back .brand__name { font-size: 25px; line-height: 27px; padding-top: 6px; }

  .divider {
    position: absolute;
    left: 243px;
    top: 83px;
    width: 1px;
    height: 69px;
    background: var(--rule);
  }
  .company-details {
    position: absolute;
    left: 253px;
    top: 95px;
    font-family: "Arimo", sans-serif;
    font-size: 13px;
    line-height: 23px;
    color: var(--brand-red);
    white-space: nowrap;
  }

  .band {
    position: absolute;
    left: 0;
    bottom: 0;
    width: 486px;
    height: 25px;
    display: block;
  }
  .band__red { fill: var(--brand-red); }
  .band__grey { fill: var(--band-grey); }
</style>
</head>
<body>
<main class="stage">

  <section class="card card--front" aria-label="Business card front">
    <div class="brand">
      <span class="brand__dot"></span>
      <p class="brand__name">Talmont<br>Constructions</p>
    </div>
    <span class="divider"></span>
    <address class="company-details" style="font-style: normal;">
      Talmont Constructions (vic) Pty Ltd<br>
      18 Quill Street Oakdene vic 3034
    </address>
    <svg class="band" viewBox="0 0 486 25" preserveAspectRatio="none" aria-hidden="true">
      <polygon class="band__red" points="0,0 234,0 241,25 0,25"/>
      <polygon class="band__grey" points="237,0 486,0 486,25 244,25"/>
    </svg>
  </section>

  <section class="card card--back" aria-label="Business card back">
    <div class="brand">
      <span class="brand__dot"></span>
      <p class="brand__name">Talmont<br>Constructions</p>
    </div>
    <svg class="band" viewBox="0 0 486 25" preserveAspectRatio="none" aria-hidden="true">
      <polygon class="band__red" points="0,0 234,0 240,25 0,25"/>
      <polygon class="band__grey" points="237,0 486,0 486,25 243,25"/>
    </svg>
  </section>

</main>
</body>
</html>
```